Digital Billboard Design: Winter Sales Event

I own a boutique furniture store in Calgary, AB (maplecrestdecor.ca) and I am looking to advertise our winter sale event on a new curved digital billboard (specs attached including required file type).

I have this billboard rented for 52-weeks so I will be looking to change the design every 4-weeks (i.e. this is intended to be an ongoing project).

The objective of this first billboard is to raise awareness around our annual winter sales event. The store itself is only a few blocks from the billboard so those commuting into downtown are just a short drive from the store.

I am looking for a fresh, clean, contemporary look that will grab your attention as you drive into downtown Calgary without presenting to much info so as to be distracting (and overwhelming -- the billboard does not need to contain all info on my current marketing material). I should also note that the store caters to a higher-end, more sophisticated clientele so the graphics need to reflect the brand (i.e. we are not Brennick Furniture or Couch Depot!).

I have attached three files:

Billboard specs
Current marketing material advertising sale (and all relevant data)
An idea that is from an American furniture store that I think is interesting

Target Market(s)

Upper middle class, sophisticated client who appreciates the finer things in life.

Industry/Entity Type

Furniture Store

Font styles to use
Sans Serif

Requirements
Must have
• Company Logo
• Winter Sales Event - 20 to 60% off
• Address: 2743 8th Ave SW
Nice to have
• Image of furniture -- see our website www.maplecrestdecor.ca -- any photo from this site can be used
Should not have
• Too much text or visual distration

```html
<!DOCTYPE html>
<html lang="en">
<head>
<meta charset="utf-8">
<title>Maplecrest Decor – Winter Sales Event Billboard</title>
<link rel="stylesheet" href="https://fonts.googleapis.com/css2?family=Arimo:wght@400;700&family=Montserrat:wght@300&display=swap">
<style>
  :root {
    --backdrop: #262626;
    --billboard-red: #c41e2a;
    --billboard-red-light: #d9212f;
    --billboard-red-dark: #a81a24;
    --ink-white: #ffffff;
    --placeholder-tint: rgba(255, 255, 255, 0.22);
  }
  html, body {
    margin: 0;
    padding: 0;
    width: 1200px;
    height: 1000px;
    overflow: hidden;
    background: var(--backdrop);
  }
  .canvas {
    position: relative;
    width: 1200px;
    height: 1000px;
  }
  .billboard {
    position: absolute;
    left: 260px;
    top: 304px;
    width: 668px;
    height: 307px;
    background:
      radial-gradient(ellipse at 50% 45%, var(--billboard-red-light) 0%, var(--billboard-red) 55%, var(--billboard-red-dark) 100%);
    color: var(--ink-white);
    overflow: hidden;
  }
  .headline {
    position: absolute;
    top: 22px;
    left: 0;
    width: 100%;
    margin: 0;
    text-align: center;
    font-family: "Arimo", Arial, sans-serif;
    font-weight: 700;
    font-size: 42px;
    line-height: 48px;
    padding-right: 10px;
    box-sizing: border-box;
  }
  .discount {
    position: absolute;
    top: 76px;
    left: 0;
    width: 100%;
    margin: 0;
    text-align: center;
    font-family: "Arimo", Arial, sans-serif;
    font-weight: 400;
    font-size: 24px;
    line-height: 30px;
    padding-right: 10px;
    box-sizing: border-box;
  }
  .snowflake {
    position: absolute;
    top: 108px;
    width: 90px;
    height: 90px;
    border-radius: 50%;
    background: var(--placeholder-tint);
  }
  .snowflake--left { left: 71px; }
  .snowflake--right { left: 518px; }
  .sofa {
    position: absolute;
    left: 212px;
    top: 116px;
    width: 244px;
    height: 86px;
    border-radius: 8px;
    background: var(--placeholder-tint);
  }
  .brand-name {
    position: absolute;
    top: 214px;
    left: 0;
    width: 100%;
    margin: 0;
    text-align: center;
    font-family: "Montserrat", Arial, sans-serif;
    font-weight: 300;
    font-size: 40px;
    line-height: 46px;
    letter-spacing: 4px;
    padding-left: 8px;
    box-sizing: border-box;
  }
  .address {
    position: absolute;
    top: 270px;
    left: 0;
    width: 100%;
    margin: 0;
    text-align: center;
    font-family: "Arimo", Arial, sans-serif;
    font-weight: 400;
    font-size: 25px;
    line-height: 30px;
    padding-left: 56px;
    box-sizing: border-box;
    text-transform: uppercase;
  }
</style>
</head>
<body>
  <main class="canvas">
    <section class="billboard">
      <h1 class="headline">Winter Sales Event</h1>
      <p class="discount">20 to 60% off</p>
      <div class="snowflake snowflake--left" role="img" aria-label="White snowflake icon"></div>
      <div class="sofa" role="img" aria-label="White sofa silhouette"></div>
      <div class="snowflake snowflake--right" role="img" aria-label="White snowflake icon"></div>
      <p class="brand-name">MAPLECREST DECOR</p>
      <p class="address">2743 8th Ave SW, Calgary, AB</p>
    </section>
  </main>
</body>
</html>
```